Brookvale Rendering Wordpress Design

I would like a design for my friends company. He has just had his logo designed and really likes the following website.

www.tlb-rendering.co.uk

Something similar to this design would be ideal but open to additional ideas. The website shown has all the relevant content.

We have 20 years of experience and can provide a number of photos for work we have done.

More photos will be provided upon request.

Target Market(s)

Homeowners

Industry/Entity Type

Trade

Font styles to use
Sans Serif

Colors
3176b5
85cae6
85abd2
eaf1f7

Requirements
Must have
• look at www.tlb-rendering.co.uk
Nice to have
Should not have
• N/A

```html
<!DOCTYPE html>
<html lang="en">
<head>
<meta charset="utf-8">
<title>Brookvale Rendering</title>
<link rel="stylesheet" href="https://fonts.googleapis.com/css2?family=League+Gothic&family=Montserrat:wght@400;500;600;700&display=swap">
<style>
:root{
  --blue:#3176b5;
  --sky:#85cae6;
  --mid:#85abd2;
  --pale:#eaf1f7;
  --ink:#4a4d54;
  --grey-bg:#e8e9eb;
  --slate:#7a7d84;
  --foot:#5f6167;
  --white:#ffffff;
  --tile:#c3c4c6;
}
*{margin:0;padding:0;box-sizing:border-box}
html,body{width:906px;height:1200px;overflow:hidden}
body{position:relative;font-family:"Montserrat",sans-serif;color:var(--ink);background:var(--white)}
.abs{position:absolute}
.display{font-family:"League Gothic",sans-serif;font-weight:400;text-transform:uppercase}

.site-header{left:0;top:0;width:906px;height:56px;background:var(--white)}
.brand{left:136px;top:12px;width:90px;text-align:center}
.brand-name{font-family:"Montserrat",sans-serif;font-weight:500;font-size:7.4px;color:var(--blue);letter-spacing:.1px;white-space:nowrap;border-top:2px solid var(--blue);border-bottom:2px solid var(--blue);padding:5px 0}
.nav a{position:absolute;top:22px;font-size:8.6px;font-weight:600;letter-spacing:.6px;color:var(--ink);text-decoration:none;white-space:nowrap}
.nav a.active{color:var(--blue);border-bottom:1.5px solid var(--blue);padding-bottom:3px}
.btn{display:block;background:var(--blue);color:var(--white);font-weight:700;border-radius:3px;text-align:center;text-transform:uppercase;letter-spacing:.4px}
.nav-register{left:666px;top:18px;width:63px;height:20px;line-height:20px;font-size:8.6px}
.search{left:760px;top:21px}

.hero{left:0;top:56px;width:906px;height:280px;background:linear-gradient(180deg,#5b6475 0%,#7d7768 45%,#5d564b 100%)}
.arrow{top:108px;width:41px;height:41px;background:rgba(40,44,52,.85);display:flex;align-items:center;justify-content:center}
.hero-title{left:165px;top:144px;font-size:42px;color:var(--white);line-height:1;letter-spacing:-.3px}
.hero-sub{left:166px;top:180px;font-size:11.2px;font-weight:500;color:var(--white)}
.hero-register{left:166px;top:212px;width:84px;height:26px;line-height:26px;font-size:11.5px}

.intro{left:0;top:336px;width:906px;height:147px;background:var(--sky);text-align:center;color:var(--white)}
.intro h2{position:absolute;left:0;width:906px;top:18px;font-family:"League Gothic",sans-serif;font-weight:400;font-size:32px;line-height:30px}
.intro .rule{position:absolute;left:441px;top:84px;width:24px;height:1px;background:var(--white)}
.intro p{position:absolute;left:153px;width:600px;top:93px;font-size:8.8px;line-height:11px;font-weight:500}
.intro p em{font-style:normal;color:#1f2a33}
.dot{top:134px;width:8px;height:8px;border-radius:50%;background:var(--white)}
.dot.off{background:var(--mid)}

.video{left:0;top:483px;width:906px;height:250px;background:linear-gradient(90deg,#6c6864 0%,#4b4641 45%,#3e3a36 100%)}
.ghost{top:128px;width:104px;height:30px;border:1px solid rgba(255,255,255,.35);background:rgba(40,40,40,.35);color:#e4e4e4;font-size:20px;display:flex;align-items:center;justify-content:center;gap:7px}

.info{left:0;top:733px;width:906px;height:232px;background:var(--grey-bg)}
.sec-head{font-size:17px;color:var(--ink);display:flex;align-items:center;gap:4px;white-space:nowrap}
.sec-head::after{content:"";flex:1;height:4px;border-top:1px solid #8b8e94;border-bottom:1px solid #8b8e94}
.duty{font-size:7.8px;font-weight:600;color:var(--blue);display:flex;align-items:center;gap:8px}
.duty i{display:inline-block;width:12px;height:12px;border-radius:50%;background:var(--blue);position:relative}
.duty i::after{content:"";position:absolute;left:3px;top:3.5px;width:3px;height:3px;border-right:1.3px solid #fff;border-top:1.3px solid #fff;transform:rotate(45deg)}
.label{font-family:"League Gothic",sans-serif;font-size:10.5px;text-transform:uppercase;color:var(--ink)}
.about{left:223px;top:96px;width:180px;font-size:7.6px;line-height:9.4px}
.join{left:109px;top:174px;font-size:16px;color:var(--ink);display:flex;align-items:center;white-space:nowrap}
.join b{color:var(--blue);font-weight:400}
.join .btn{font-family:"Montserrat",sans-serif;font-size:7.4px;padding:0 7px;height:18px;line-height:18px;margin-left:8px}

.news-item{left:533px;width:300px;display:flex;gap:10px}
.cal{width:34px;height:34px;flex:none}
.news-item h4{font-size:9.2px;font-weight:600;color:var(--blue);text-transform:uppercase;letter-spacing:.2px;margin-top:2px}
.news-item p{font-size:7.6px;line-height:9.6px;margin-top:2px}
.news-item p b{font-weight:700}

.stripe{left:0;top:965px;width:906px;height:8px;background:var(--sky)}
.clients{left:0;top:973px;width:906px;height:188px;background:var(--slate)}
.clients h3{position:absolute;left:118px;top:19px;font-size:17px;color:var(--white)}
.tile{top:69px;width:72px;height:72px;background:var(--white);font-family:"League Gothic",sans-serif;font-size:34px;color:#333;display:flex;align-items:center;justify-content:center}
.tile.alt{background:var(--tile)}

.site-footer{left:0;top:1161px;width:906px;height:39px;background:var(--foot)}
.copy{left:54px;top:14px;font-size:7.6px;color:var(--white)}
.social{top:16px;width:9px;height:9px;border-radius:50%;background:#d9dadd}
.tip{left:723px;top:-8px;background:#2d2f33;color:#ddd;font-size:6.4px;padding:3px 6px;border-radius:1px}
</style>
</head>
<body>

<header class="site-header abs">
  <div class="brand abs"><div class="brand-name">BROOKVALE RENDERING</div></div>
  <nav class="nav">
    <a class="active" style="left:275px">WHO WE ARE</a>
    <a style="left:366px">WHAT WE DO</a>
    <a style="left:467px">NEWS&amp;UPDATES</a>
    <a style="left:572px">CONTACT US</a>
  </nav>
  <a class="btn nav-register abs">Register</a>
  <svg class="search abs" width="10" height="10" viewBox="0 0 10 10"><circle cx="4" cy="4" r="3" fill="none" stroke="#555" stroke-width="1.3"/><line x1="6.2" y1="6.2" x2="9" y2="9" stroke="#555" stroke-width="1.4"/></svg>
</header>

<section class="hero abs" role="img" aria-label="Photo of a stone house with a rounded rendered tower under a blue sky">
  <div class="arrow abs" style="left:0"><svg width="10" height="14" viewBox="0 0 10 14"><polyline points="8,1 2,7 8,13" fill="none" stroke="#fff" stroke-width="1.6"/></svg></div>
  <div class="arrow abs" style="left:865px"><svg width="10" height="14" viewBox="0 0 10 14"><polyline points="2,1 8,7 2,13" fill="none" stroke="#fff" stroke-width="1.6"/></svg></div>
  <h1 class="hero-title display abs">The things we do best</h1>
  <p class="hero-sub abs">We are specialists in all 6 of the following areas</p>
  <a class="btn hero-register abs">Register</a>
</section>

<section class="intro abs">
  <h2>Far far away, behind the word mountains, far from the<br>countries Vokalia and Consonantia, there live the blind texts.</h2>
  <span class="rule"></span>
  <p>Far far away, behind the word <em>mountains</em>, far from the countries Vokalia and Consonantia, there live the blind texts. Separated they live in Bookmarksgrove right at the coast of the Semantics, a large language ocean. A small river named Duden flows by their place and supplies it with the necessary regelialia. It is a paradisematic country, in which roasted parts of sentences fly into your mouth. Even the all-powerful Pointing has no control about the blind texts.</p>
  <span class="dot abs" style="left:713px"></span>
  <span class="dot off abs" style="left:726px"></span>
</section>

<section class="video abs" role="img" aria-label="Photo of a plasterer working on a wall inside a room under renovation">
  <a class="ghost display abs" style="left:486px">Explore</a>
  <a class="ghost display abs" style="left:622px"><svg width="8" height="11" viewBox="0 0 8 11"><polygon points="0,0 8,5.5 0,11" fill="#ddd"/></svg>Play video</a>
</section>

<section class="info abs">
  <h3 class="sec-head display abs" style="left:108px;top:26px;width:298px">Brookvale Duties</h3>
  <div class="duty abs" style="left:109px;top:61px"><i></i>Wall Plaster</div>
  <div class="duty abs" style="left:109px;top:83px"><i></i>Ceiling Plaster</div>
  <div class="abs label" style="left:223px;top:62px">Difficulty: <span style="font-family:Montserrat,sans-serif;font-size:7.6px;letter-spacing:.5px;color:#666">★★★☆☆</span></div>
  <p class="about abs"><span class="label">About the role:</span> Far far away, behind the word mountains, far from the countries Vokalia and Consonantia, there live the blind texts. They live in Bookmarksgrove right at the coast of the Semantics, a large language ocean.</p>
  <div class="join display abs">Join our&nbsp;<b>XXX,XXX</b>&nbsp;happy &amp; content clients <a class="btn">Register</a></div>

  <h3 class="sec-head display abs" style="left:531px;top:26px;width:298px">Brookvale News</h3>

  <div class="news-item abs" style="top:52px">
    <svg class="cal" viewBox="0 0 34 34"><rect x="1.5" y="4" width="31" height="28" rx="2" fill="none" stroke="#555" stroke-width="2"/><line x1="1.5" y1="10" x2="32.5" y2="10" stroke="#555" stroke-width="2"/><rect x="8" y="1" width="3" height="6" fill="#555"/><rect x="23" y="1" width="3" height="6" fill="#555"/><text x="17" y="19" font-family="Montserrat,sans-serif" font-weight="600" font-size="7" fill="#555" text-anchor="middle">SEP</text><text x="17" y="29" font-family="Montserrat,sans-serif" font-weight="600" font-size="9.5" fill="#555" text-anchor="middle">10</text></svg>
    <div><h4>Brookvale wins award</h4><p>Brookvale wins award for developing new device for the disabled community.... <b>READ MORE</b></p></div>
  </div>
  <div class="news-item abs" style="top:98px">
    <svg class="cal" viewBox="0 0 34 34"><rect x="1.5" y="4" width="31" height="28" rx="2" fill="none" stroke="#555" stroke-width="2"/><line x1="1.5" y1="10" x2="32.5" y2="10" stroke="#555" stroke-width="2"/><rect x="8" y="1" width="3" height="6" fill="#555"/><rect x="23" y="1" width="3" height="6" fill="#555"/><text x="17" y="19" font-family="Montserrat,sans-serif" font-weight="600" font-size="7" fill="#555" text-anchor="middle">AUG</text><text x="17" y="29" font-family="Montserrat,sans-serif" font-weight="600" font-size="9.5" fill="#555" text-anchor="middle">18</text></svg>
    <div><h4>Brookvale gets praise from the community</h4><p>Community praises Brookvale for changing attitudes of the youth community.... <b>READ MORE</b></p></div>
  </div>
  <div class="news-item abs" style="top:142px">
    <svg class="cal" viewBox="0 0 34 34"><rect x="1.5" y="4" width="31" height="28" rx="2" fill="none" stroke="#555" stroke-width="2"/><line x1="1.5" y1="10" x2="32.5" y2="10" stroke="#555" stroke-width="2"/><rect x="8" y="1" width="3" height="6" fill="#555"/><rect x="23" y="1" width="3" height="6" fill="#555"/><text x="17" y="19" font-family="Montserrat,sans-serif" font-weight="600" font-size="7" fill="#555" text-anchor="middle">AUG</text><text x="17" y="29" font-family="Montserrat,sans-serif" font-weight="600" font-size="9.5" fill="#555" text-anchor="middle">08</text></svg>
    <div><h4>Brookvale winner 2016</h4><p>Brookvale wins the top platering company in the year 2016. .according to the community... <b>READ MORE</b></p></div>
  </div>
</section>

<div class="stripe abs"></div>

<section class="clients abs">
  <h3 class="display">Major clients</h3>
  <div class="tile abs" style="left:155px">logo</div>
  <div class="tile alt abs" style="left:262px">logo</div>
  <div class="tile abs" style="left:369px">logo</div>
  <div class="tile alt abs" style="left:475px">logo</div>
  <div class="tile abs" style="left:583px">logo</div>
  <div class="tile alt abs" style="left:690px">logo</div>
</section>

<footer class="site-footer abs">
  <p class="copy abs">Copyright 2015 Halverton Studio | &nbsp;All Rights Reserved</p>
  <span class="tip abs">Follow us</span>
  <span class="social abs" style="left:735px;opacity:.6"></span>
  <span class="social abs" style="left:759px"></span>
  <span class="social abs" style="left:784px"></span>
  <span class="social abs" style="left:809px"></span>
  <span class="social abs" style="left:834px"></span>
</footer>

</body>
</html>
```